New Business card with our new logo

NEW BUSINESS CARDS wth our new logo

Want a sophisticated look. Probably in deep purple ink. (but we are open)
Would like something that looks expensive. Do not want a cutsie food look.
Not sure what more information I can offer. If you have any please contact me.

NAME - Iris Dunmore Halloway, Owner
415-273 8190
iris@velvetplatterco.example
velvetplatterco.example

Target Market(s)

not sure what your are asking?

Industry/Entity Type

Business

Contact Information for Business Card

Logo + informaiton
Want a sophisticated look if possible. The cards are for women

Font styles to use
Serif

Colors
886aae

Requirements
Must have
• Iris Dunmore Halloway, Owner
• 415-273 8190
• iris@velvetplatterco.example
• velvetplatterco.example
Nice to have
• suprise me
Should not have
• No cute food images, chef hat, knives, forks, etc.

```html
<!DOCTYPE html>
<html lang="en">
<head>
<meta charset="utf-8">
<title>Velvet Platter – Business Card</title>
<link rel="stylesheet" href="https://fonts.googleapis.com/css2?family=Libre+Baskerville:wght@400;700&display=swap">
<style>
  :root {
    --stage: #6a6a6a;
    --ink-deep: #2b1742;
    --paper: #f4eff6;
    --plum: #5a2d86;
    --violet: #7c4ba8;
    --band-1: #5b2d8a;
    --band-2: #6f3ca1;
    --band-3: #8a5cb8;
    --lime: #a6d24b;
    --white: #ffffff;
  }
  html, body {
    margin: 0;
    width: 1064px;
    height: 1200px;
    overflow: hidden;
    background: var(--stage);
  }
  .stage {
    width: 1064px;
    height: 1200px;
    display: flex;
    align-items: center;
    justify-content: center;
  }
  .business-card {
    width: 960px;
    height: 576px;
    display: block;
    box-shadow: 0 10px 30px rgba(0,0,0,.35);
  }
  .card-text { font-family: "Libre Baskerville", "Times New Roman", serif; }
  .holder-name { fill: var(--plum); font-weight: 700; font-size: 17px; }
  .holder-role { fill: var(--white); font-weight: 700; font-size: 15px; }
  .contact-line { fill: var(--white); font-weight: 700; font-size: 12.5px; }
  .brand-name { fill: var(--violet); font-weight: 400; font-size: 18px; letter-spacing: 0.5px; }
  .brand-mark { fill: none; stroke: var(--violet); stroke-width: 1.4; }
  .icon-disc { fill: var(--lime); }
  .icon-glyph { fill: none; stroke: var(--ink-deep); stroke-width: 1.6; stroke-linecap: round; stroke-linejoin: round; }
  .icon-solid { fill: var(--ink-deep); }
</style>
</head>
<body>
<main class="stage">
  <svg class="business-card" viewBox="0 0 612 367" xmlns="http://www.w3.org/2000/svg" aria-label="Velvet Platter business card for Iris Dunmore Halloway">
    <defs>
      <clipPath id="front-panel-clip">
        <circle cx="-188" cy="175" r="448"/>
      </clipPath>
      <clipPath id="upper-arc-clip">
        <rect x="0" y="0" width="612" height="300"/>
      </clipPath>
    </defs>

    <rect class="card-backdrop" x="0" y="0" width="612" height="367" fill="var(--ink-deep)"/>

    <g clip-path="url(#upper-arc-clip)">
      <circle class="accent-arc" cx="-188" cy="175" r="460" fill="var(--violet)"/>
    </g>
    <circle class="lime-arc" cx="-188" cy="175" r="452" fill="var(--lime)"/>
    <circle class="paper-panel" cx="-188" cy="175" r="448" fill="var(--paper)"/>

    <g class="colour-bands" clip-path="url(#front-panel-clip)">
      <rect x="0" y="303" width="85" height="45" fill="var(--band-1)"/>
      <rect x="85" y="303" width="80" height="45" fill="var(--band-2)"/>
      <rect x="165" y="303" width="110" height="45" fill="var(--band-3)"/>
    </g>

    <g class="brand">
      <circle class="brand-mark" cx="30" cy="179" r="7"/>
      <text class="card-text brand-name" x="45" y="185">VELVET PLATTER</text>
    </g>

    <rect class="name-band" x="270" y="80" width="342" height="31" fill="var(--paper)"/>
    <text class="card-text holder-name" x="588" y="102" text-anchor="end">Iris Dunmore Halloway</text>
    <text class="card-text holder-role" x="588" y="143" text-anchor="end">Owner</text>

    <g class="contact-phone">
      <text class="card-text contact-line" x="550" y="191" text-anchor="end">415-273 8190</text>
      <circle class="icon-disc" cx="572" cy="186" r="13"/>
      <path class="icon-solid" d="M566.5 179.5 l3 -1 l2 4.5 l-2 1.5 q1.5 3 4.5 4.5 l1.5 -2 l4.5 2 l-1 3 q-1 1.5 -3 1 q-8 -2 -11 -10 q-0.5 -2 1 -3.5z"/>
    </g>
    <g class="contact-email">
      <text class="card-text contact-line" x="550" y="237" text-anchor="end">iris@velvetplatterco.example</text>
      <circle class="icon-disc" cx="572" cy="232" r="13"/>
      <rect class="icon-glyph" x="564.5" y="227" width="15" height="10" rx="1"/>
      <path class="icon-glyph" d="M564.5 227 l7.5 6 l7.5 -6"/>
    </g>
    <g class="contact-web">
      <text class="card-text contact-line" x="550" y="283" text-anchor="end">velvetplatterco.example</text>
      <circle class="icon-disc" cx="572" cy="278" r="13"/>
      <circle class="icon-glyph" cx="572" cy="278" r="7.5"/>
      <ellipse class="icon-glyph" cx="572" cy="278" rx="3.2" ry="7.5"/>
      <path class="icon-glyph" d="M564.5 278 h15"/>
    </g>
  </svg>
</main>
</body>
</html>
```